Penny Harvest

Logo and general packaging design for premium quality, price conscious super foods.

Initial product portfolio includes:

Organic Raw Chia Seeds - Resealable plastic bags with 3 x 5 label.
Organic Cold Pressed Coconut Oil (plastic jar) - 2.5 x 6.5 label

The design should be transferable to additional products.

Project requirements:

The design should be simple and the core trade dress should be no more than 2 or 3 colors. The logo should reproduce well in black/1 color.

The idea of this design is to convey quality and simplicity, like a "no frills", premium quality brand.

Deliverable: fully editable (text and illustration):

Logo.

Basic Jar label design.

Basic Bag label design.

Target Market(s)

Educated women aged 22-45

Industry/Entity Type

Plastic

Requirements
Must have
• Clear, simple logo, delivered in vector form, 1 color/black.
• Use of logo on 1 jar label and 1 bag label, each with product name and space for required and optional marketing content.
Nice to have
• Additional iterations of the design to demonstrate your concept of how we will visually vary additional items in jars and bags.
• i.e. What an additional product in a bag would look like for purposes of brand consistency and product differentiation on shelf or online in e-store.
Should not have
• overly detailed graphics that don't scale well and/or may be hard to read or understand. 4 color design elements (except to simiulate how the product may look through the clear jar or bag or how the product may be placed in a simulated surrounding or ad.

```html
<!DOCTYPE html>
<html lang="en">
<head>
<meta charset="utf-8">
<title>Penny Harvest – Chia Seed Pouch Label</title>
<link rel="stylesheet" href="https://fonts.googleapis.com/css2?family=Montserrat:wght@500;600&family=Zilla+Slab:wght@400;500&display=swap">
<style>
  :root {
    --page-bg: #ffffff;
    --pouch-light: #f6e4b8;
    --pouch-mid: #ecd095;
    --pouch-edge: #ddbb78;
    --ink-brown: #4a3a2c;
    --badge-brown: #4b3a2d;
    --badge-text: #ffffff;
    --seed-dark: #3e4042;
    --seed-light: #7d7f81;
  }
  * { margin: 0; padding: 0; box-sizing: border-box; }
  html, body {
    width: 1200px; height: 900px; overflow: hidden;
    background: var(--page-bg);
  }
  .canvas { position: relative; width: 1200px; height: 900px; }
  .pouch {
    position: absolute; left: 472px; top: 92px;
    width: 446px; height: 678px;
    border-radius: 14px 14px 10px 10px;
    background: radial-gradient(ellipse at 50% 55%, var(--pouch-light) 0%, var(--pouch-mid) 75%, var(--pouch-edge) 100%);
    color: var(--ink-brown);
  }
  .hang-hole {
    position: absolute; left: 160px; top: 33px;
    width: 126px; height: 22px; border-radius: 11px;
    background: var(--page-bg);
  }
  .seal-line {
    position: absolute; left: 0; right: 0; height: 1px;
    background: rgba(120, 90, 40, 0.18);
  }
  .seal-line.top { top: 108px; }
  .seal-line.zip { top: 153px; }
  .brand {
    position: absolute; left: 0; right: 0; top: 238px;
    text-align: center;
    font-family: "Montserrat", sans-serif; font-weight: 500;
    font-size: 28px; letter-spacing: 0.5px;
    color: var(--ink-brown);
  }
  .product-name {
    position: absolute; left: 0; right: 0; top: 300px;
    text-align: center;
    font-family: "Zilla Slab", serif; font-weight: 500;
    font-size: 54px; letter-spacing: 1.5px;
    color: var(--ink-brown);
  }
  .seed-window {
    position: absolute; left: 123px; top: 370px;
    width: 205px; height: 198px;
  }
  .badge {
    position: absolute; left: 278px; top: 463px;
    width: 102px; height: 102px; border-radius: 50%;
    background: var(--badge-brown); color: var(--badge-text);
    display: flex; flex-direction: column; align-items: center; justify-content: center;
    font-family: "Montserrat", sans-serif; font-weight: 600;
    font-size: 16px; line-height: 1.25; text-align: center;
  }
  .claims {
    position: absolute; left: 0; right: 0; top: 587px;
    text-align: center;
    font-family: "Zilla Slab", serif; font-weight: 400;
    font-size: 12px; letter-spacing: 0.3px;
    color: var(--ink-brown);
  }
  .net-weight {
    position: absolute; right: 78px; top: 630px;
    font-family: "Zilla Slab", serif; font-weight: 400;
    font-size: 22px; color: var(--ink-brown);
  }
</style>
</head>
<body>
<main class="canvas">
  <section class="pouch">
    <div class="hang-hole"></div>
    <div class="seal-line top"></div>
    <div class="seal-line zip"></div>

    <h1 class="brand">Penny Harvest</h1>
    <h2 class="product-name">CHIA SEED</h2>

    <svg class="seed-window" viewBox="0 0 205 198" role="img" aria-label="Window illustration showing black and white chia seeds">
      <defs>
        <linearGradient id="seedTone" x1="0" y1="0" x2="1" y2="1">
          <stop offset="0" stop-color="var(--seed-light)"/>
          <stop offset="1" stop-color="var(--seed-dark)"/>
        </linearGradient>
      </defs>
      <rect x="0" y="0" width="205" height="198" rx="12" fill="url(#seedTone)"/>
    </svg>

    <div class="badge"><span>Organic</span><span>SUPER</span><span>FOOD</span></div>

    <p class="claims">Omega 3 &nbsp;|&nbsp; Dietary Fibre &nbsp;|&nbsp; Protein &nbsp;|&nbsp; Antioxidants</p>
    <p class="net-weight">500g</p>
  </section>
</main>
</body>
</html>
```